CoverHarbor Gap Insurance InfoGraphic

We need an infographic detailing what Gap insurance is, the types, and who needs it. All of this information can be found in the attached report. Please adhere to the same branding style as our website, www.coverharbor-example.net

Target Market(s)

people age 64+ and their families

Industry/Entity Type

Insurance

Requirements
Must have
• Must cover multiple facets of gap insurance, not just "what is it"

```html
<!DOCTYPE html>
<html lang="en">
<head>
<meta charset="utf-8">
<title>CoverHarbor – Medigap Insurance Guide</title>
<link href="https://fonts.googleapis.com/css2?family=Source+Sans+3:wght@600&display=swap" rel="stylesheet">
<style>
  :root {
    --bg: #ffffff;
    --navy: #03223a;
    --orange: #ff8000;
    --ink: #0d2236;
    --white: #ffffff;
    --plum-edge: #4a0030;
    --plum-mid: #830a5a;
    --plum-line: #8c1c6a;
    --blue-light: #5aaede;
    --blue-deep: #145c94;
    --blue-line: #3fb4e6;
    --ruby-light: #c55a72;
    --ruby-deep: #8c1024;
    --frame: #dcdcdc;
  }
  html, body {
    margin: 0;
    width: 923px;
    height: 1200px;
    overflow: hidden;
    background: var(--bg);
  }
  .infographic { display: block; width: 923px; height: 1200px; }
  .infographic text {
    font-family: "Source Sans 3", sans-serif;
    font-weight: 600;
    text-anchor: middle;
    dominant-baseline: middle;
  }
  .label { fill: var(--white); font-size: 35px; }
  .hex-label { fill: var(--white); font-size: 33px; }
  .hero-label { fill: var(--white); font-size: 36px; }
  .note { fill: var(--ink); font-size: 35px; text-anchor: start !important; }
  .arrow-dark { fill: var(--navy); }
  .arrow-orange { fill: var(--orange); }
  .banner { fill: url(#plum); stroke: var(--plum-line); stroke-width: 3; }
  .hex-frame { fill: var(--frame); }
  .hex-blue { fill: url(#blue); stroke: var(--blue-line); stroke-width: 3; }
  .hex-ruby { fill: url(#ruby); stroke: #e0455e; stroke-width: 3; }
  .bracket { fill: none; stroke: var(--orange); stroke-width: 22; }
</style>
</head>
<body>
<svg class="infographic" viewBox="0 0 1678 2213" preserveAspectRatio="xMidYMid meet" xmlns="http://www.w3.org/2000/svg">
  <defs>
    <radialGradient id="plum" cx="50%" cy="50%" r="60%">
      <stop offset="0" stop-color="var(--plum-mid)"/>
      <stop offset="1" stop-color="var(--plum-edge)"/>
    </radialGradient>
    <linearGradient id="blue" x1="0" y1="0" x2="0" y2="1">
      <stop offset="0" stop-color="var(--blue-light)"/>
      <stop offset="0.55" stop-color="#2390cf"/>
      <stop offset="1" stop-color="var(--blue-deep)"/>
    </linearGradient>
    <linearGradient id="ruby" x1="0" y1="0" x2="0.4" y2="1">
      <stop offset="0" stop-color="var(--ruby-light)"/>
      <stop offset="0.6" stop-color="#c0203a"/>
      <stop offset="1" stop-color="var(--ruby-deep)"/>
    </linearGradient>
  </defs>

  <!-- Top hub -->
  <g class="hub">
    <polygon class="hex-frame" points="690,178 765,48 915,48 990,178 915,308 765,308"/>
    <polygon class="hex-ruby" points="715,178 777,70 903,70 965,178 903,286 777,286"/>
    <text class="hero-label" x="838" y="157">Medigap</text>
    <text class="hero-label" x="840" y="199">Insurance</text>
  </g>
  <polygon class="arrow-dark" points="662,158 476,158 476,220 450,220 492,284 534,220 508,220 508,190 662,190"/>
  <polygon class="arrow-dark" points="1017,158 1203,158 1203,220 1229,220 1188,284 1146,220 1172,220 1172,190 1017,190"/>
  <polygon class="arrow-orange" points="820,342 857,342 857,636 886,636 838,708 790,636 820,636"/>

  <!-- Who can buy -->
  <polygon class="banner" points="292,302 695,302 723,353 695,405 292,405 263,353"/>
  <text class="label" x="493" y="353">Who Can Buy?</text>
  <polygon class="arrow-orange" points="467,426 502,426 502,472 530,472 485,542 439,472 467,472"/>
  <polygon class="hex-frame" points="377,648 433,548 543,548 603,648 543,748 433,748"/>
  <polygon class="hex-blue" points="394,648 441,566 533,566 580,648 533,730 441,730"/>
  <text class="hex-label" x="485" y="649">Conditions</text>
  <path class="bracket" d="M366 640 H185 V868 H222 M185 806 H222"/>
  <polygon class="arrow-orange" points="220,785 255,806 220,828"/>
  <polygon class="arrow-orange" points="220,848 255,870 220,892"/>
  <text class="note" x="270" y="807">Your age 65</text>
  <text class="note" x="270" y="868">You are enrolled in</text>
  <text class="note" x="277" y="911">medicare Parts A &amp; B</text>

  <!-- When can buy -->
  <polygon class="banner" points="987,302 1390,302 1418,353 1390,405 987,405 958,353"/>
  <text class="label" x="1188" y="353">When Can Buy?</text>
  <polygon class="arrow-orange" points="1171,426 1206,426 1206,472 1234,472 1188,542 1143,472 1171,472"/>
  <polygon class="banner" points="991,548 1394,548 1422,600 1394,651 991,651 962,600"/>
  <text class="label" x="1188" y="578">During 6 month</text>
  <text class="label" x="1192" y="620">Medigap open period</text>

  <!-- Main path -->
  <polygon class="banner" points="637,732 1040,732 1068,783 1040,835 637,835 608,783"/>
  <text class="label" x="838" y="783">Already have Plan?</text>
  <polygon class="arrow-orange" points="820,854 855,854 855,900 883,900 838,970 793,900 820,900"/>
  <polygon class="banner" points="637,991 1040,991 1068,1042 1040,1094 637,1094 608,1042"/>
  <text class="label" x="838" y="1042">Medical Treatment?</text>
  <polygon class="arrow-orange" points="820,1110 855,1110 855,1156 883,1156 838,1226 793,1156 820,1156"/>

  <!-- Two step process -->
  <polygon class="hex-frame" points="743,1313 790,1231 886,1231 933,1313 886,1395 790,1395"/>
  <polygon class="hex-blue" points="758,1313 798,1245 878,1245 918,1313 878,1381 798,1381"/>
  <text class="hex-label" x="838" y="1295">2 Step</text>
  <text class="hex-label" x="838" y="1333">Process</text>
  <polygon class="arrow-dark" points="727,1304 540,1304 540,1366 515,1366 557,1430 599,1366 572,1366 572,1336 727,1336"/>
  <polygon class="arrow-dark" points="960,1302 1146,1302 1146,1365 1171,1365 1130,1428 1088,1365 1113,1365 1113,1335 960,1335"/>

  <polygon class="hex-frame" points="463,1525 510,1443 606,1443 653,1525 606,1607 510,1607"/>
  <polygon class="hex-blue" points="480,1525 519,1457 597,1457 636,1525 597,1593 519,1593"/>
  <text class="hex-label" x="557" y="1526">Step 1</text>
  <polygon class="hex-frame" points="1035,1525 1082,1443 1178,1443 1225,1525 1178,1607 1082,1607"/>
  <polygon class="hex-blue" points="1052,1525 1091,1457 1169,1457 1208,1525 1169,1593 1091,1593"/>
  <text class="hex-label" x="1130" y="1526">Step 2</text>

  <polygon class="arrow-orange" points="538,1635 573,1635 573,1681 601,1681 555,1751 510,1681 538,1681"/>
  <polygon class="arrow-orange" points="1116,1635 1151,1635 1151,1681 1179,1681 1133,1751 1088,1681 1116,1681"/>

  <polygon class="banner" points="374,1768 800,1768 830,1823 800,1878 374,1878 343,1823"/>
  <text class="label" x="583" y="1822">Medicare coverage approves</text>
  <polygon class="banner" points="934,1773 1360,1773 1390,1828 1360,1883 934,1883 903,1828"/>
  <text class="label" x="1144" y="1808">Go to your Medigap</text>
  <text class="label" x="1147" y="1850">Insurance Plan</text>

  <polygon class="arrow-dark" points="1135,1898 1168,1898 1168,2033 1058,2033 1058,2059 993,2016 1058,1973 1058,2000 1135,2000"/>
  <polygon class="banner" points="511,1963 936,1963 966,2018 936,2073 511,2073 480,2018"/>
  <text class="label" x="723" y="2018">Recieve your rest of Bill</text>
</svg>
</body>
</html>
```